Design a new jar label for a successful company

We are seeking a fresh label design that will be applied to a glass jar containing our high quality dried flower. We are a company based out of Washington State and we mainly sell dried herbs and oil extracts. The brand is "Copper Hollow" and the product is "Copper Hollow - Handcrafted Flower". I'd like to start with Black/Chrome as the color scheme, but we are open to other suggestions (for example dark purple instead of black). This will be professionally printed on a glossy label and the chrome or auxiliary colors can/will printed with a metallic foil.

BASIC REQUIREMENTS:

Size: 1.25" H x 2.5" L

Colors: Black and chrome. Preferably use a black background and make the logo/text chrome. Open to suggestions.

Margin: Please do not place any text within 1/16" around the edges to allow for deviation during die cutting process.

Logo: Use the Copper Hollow shield as the center piece.

Required text: State "Handcrafted Flower" somewhere below the logo. Discretely place "QZTLN.COM" somewhere on the label.

Industry/Entity Type

Retail

Font styles to use
Other font styles liked:
• FestivoLettersNo1.otf

Requirements
Must have
• The following warning most appear on the label. Please see attached graphic and also be sure to include the "21 and over" circular icon if possible:
• "Warning: This product has intoxicating effects and may be habit forming. Marijuana can impair concentration, coordination, and judgement. Do not operate a vehicle or machinery under the influence of this drug. There may be health risks associated with consumption of this product."
• "For use only by adults twenty-one and older. Keep out of reach of children."
• Note: You can use the circular 21 and over warning shown in the attached example instead of typing the text out.
Nice to have
• Fonts used - Dorel Vasko - FestivoLettersNo1.otf (This is the logo font.)
• Minion Pro - this is our standard copy font

```html
<!DOCTYPE html>
<html lang="en">
<head>
<meta charset="utf-8">
<title>Copper Hollow – Handcrafted Flower Jar Labels</title>
<link href="https://fonts.googleapis.com/css2?family=Encode+Sans+Condensed:wght@300;400;500;600&display=swap" rel="stylesheet">
<style>
  :root {
    --canvas: #ffffff;
    --label-purple: #1e0a36;
    --label-green: #0a140b;
    --label-maroon: #2a0c11;
    --chrome: #cfcfd3;
    --ink-light: #f4f4f4;
    --age-pink: #e6197f;
    --floral-tone: rgba(255, 255, 255, 0.16);
  }
  * { box-sizing: border-box; margin: 0; padding: 0; }
  html, body {
    width: 1200px;
    height: 1100px;
    overflow: hidden;
    background: var(--canvas);
  }
  .sheet {
    position: relative;
    width: 1200px;
    height: 1100px;
    font-family: "Encode Sans Condensed", "Arial Narrow", sans-serif;
  }
  .jar-label {
    position: absolute;
    width: 612px;
    height: 304px;
    overflow: hidden;
    color: var(--ink-light);
  }
  .jar-label--purple { left: 277px; top: 18px;  background: var(--label-purple); }
  .jar-label--green  { left: 280px; top: 400px; background: var(--label-green); }
  .jar-label--maroon { left: 283px; top: 756px; background: var(--label-maroon); }

  .floral-band {
    position: absolute;
    left: 0; right: 0; bottom: 0;
    height: 78px;
    background: linear-gradient(to top, var(--floral-tone), rgba(255,255,255,0.04));
  }

  .product-title {
    position: absolute;
    left: 14px;
    top: 20px;
    width: 62px;
    height: 198px;
  }
  .product-title__inner {
    position: absolute;
    left: 0; top: 198px;
    width: 198px;
    transform: rotate(-90deg);
    transform-origin: 0 0;
    text-align: right;
    line-height: 1;
  }
  .product-title__tier {
    display: block;
    font-size: 22px;
    font-weight: 400;
    letter-spacing: 0.2px;
    padding-right: 0;
  }
  .product-title__kind {
    display: block;
    margin-top: 2px;
    font-size: 37px;
    font-weight: 400;
    letter-spacing: 1px;
    padding-right: 30px;
  }

  .brand-mark {
    position: absolute;
    left: 96px;
    top: 22px;
    width: 190px;
    height: 240px;
    display: flex;
    flex-direction: column;
    align-items: center;
    justify-content: center;
    text-align: center;
  }
  .brand-mark__name {
    font-size: 38px;
    font-weight: 600;
    line-height: 1.1;
    letter-spacing: 1px;
    text-transform: uppercase;
    color: var(--chrome);
  }

  .warning-copy {
    position: absolute;
    left: 360px;
    top: 16px;
    width: 232px;
    font-size: 14.6px;
    font-weight: 300;
    line-height: 17px;
    text-align: justify;
    text-align-last: left;
  }
  .child-notice {
    position: absolute;
    left: 359px;
    top: 177px;
    width: 180px;
    font-size: 15.5px;
    font-weight: 400;
    line-height: 20px;
    text-transform: uppercase;
  }
  .site-url {
    position: absolute;
    left: 360px;
    top: 224px;
    font-size: 19px;
    font-weight: 400;
    letter-spacing: 3.6px;
  }
  .age-badge {
    position: absolute;
    left: 531px;
    top: 182px;
    width: 68px;
    height: 68px;
  }
</style>
</head>
<body>
<main class="sheet">

  <section class="jar-label jar-label--purple" aria-label="Jar label, purple colourway">
    <div class="floral-band" role="img" aria-label="Line-drawn floral pattern along the bottom edge"></div>
    <div class="product-title"><div class="product-title__inner"><span class="product-title__tier">PREMIUM QUALITY</span><span class="product-title__kind">FLOWER</span></div></div>
    <div class="brand-mark"><span class="brand-mark__name">Copper<br>Hollow</span></div>
    <p class="warning-copy">WARNING: This product has intoxicating effects and may be habit forming. Marijuana can impair concentration, coordination, and judgement. Do not operate a vehicle or machinery under the influence of this drug. There may be health risks associated with consumption of this product.</p>
    <p class="child-notice">Keep out of reach of children</p>
    <p class="site-url">QZTLN.COM</p>
    <svg class="age-badge" viewBox="0 0 68 68" aria-label="For use only by adults 21 or older">
      <defs><path id="ring-a" d="M34,34 m-24,0 a24,24 0 1,1 48,0 a24,24 0 1,1 -48,0"/></defs>
      <text fill="var(--age-pink)" font-size="7.4" font-weight="600" letter-spacing="0.3"><textPath href="#ring-a">FOR USE ONLY BY ADULTS 21 OR OLDER.</textPath></text>
      <text x="34" y="43" text-anchor="middle" fill="var(--age-pink)" font-size="27" font-weight="600">21</text>
    </svg>
  </section>

  <section class="jar-label jar-label--green" aria-label="Jar label, green colourway">
    <div class="floral-band" role="img" aria-label="Line-drawn floral pattern along the bottom edge"></div>
    <div class="product-title"><div class="product-title__inner"><span class="product-title__tier">PREMIUM QUALITY</span><span class="product-title__kind">FLOWER</span></div></div>
    <div class="brand-mark"><span class="brand-mark__name">Copper<br>Hollow</span></div>
    <p class="warning-copy">WARNING: This product has intoxicating effects and may be habit forming. Marijuana can impair concentration, coordination, and judgement. Do not operate a vehicle or machinery under the influence of this drug. There may be health risks associated with consumption of this product.</p>
    <p class="child-notice">Keep out of reach of children</p>
    <p class="site-url">QZTLN.COM</p>
    <svg class="age-badge" viewBox="0 0 68 68" aria-label="For use only by adults 21 or older">
      <defs><path id="ring-b" d="M34,34 m-24,0 a24,24 0 1,1 48,0 a24,24 0 1,1 -48,0"/></defs>
      <text fill="var(--age-pink)" font-size="7.4" font-weight="600" letter-spacing="0.3"><textPath href="#ring-b">FOR USE ONLY BY ADULTS 21 OR OLDER.</textPath></text>
      <text x="34" y="43" text-anchor="middle" fill="var(--age-pink)" font-size="27" font-weight="600">21</text>
    </svg>
  </section>

  <section class="jar-label jar-label--maroon" aria-label="Jar label, maroon colourway">
    <div class="floral-band" role="img" aria-label="Line-drawn floral pattern along the bottom edge"></div>
    <div class="product-title"><div class="product-title__inner"><span class="product-title__tier">PREMIUM QUALITY</span><span class="product-title__kind">FLOWER</span></div></div>
    <div class="brand-mark"><span class="brand-mark__name">Copper<br>Hollow</span></div>
    <p class="warning-copy">WARNING: This product has intoxicating effects and may be habit forming. Marijuana can impair concentration, coordination, and judgement. Do not operate a vehicle or machinery under the influence of this drug. There may be health risks associated with consumption of this product.</p>
    <p class="child-notice">Keep out of reach of children</p>
    <p class="site-url">QZTLN.COM</p>
    <svg class="age-badge" viewBox="0 0 68 68" aria-label="For use only by adults 21 or older">
      <defs><path id="ring-c" d="M34,34 m-24,0 a24,24 0 1,1 48,0 a24,24 0 1,1 -48,0"/></defs>
      <text fill="var(--age-pink)" font-size="7.4" font-weight="600" letter-spacing="0.3"><textPath href="#ring-c">FOR USE ONLY BY ADULTS 21 OR OLDER.</textPath></text>
      <text x="34" y="43" text-anchor="middle" fill="var(--age-pink)" font-size="27" font-weight="600">21</text>
    </svg>
  </section>

</main>
</body>
</html>
```